Wordpress Design Project

Hi- We are seeking a Wordpress Theme Design that will best serve as an introduction of our company, Pellwick Trading Co, to potential international clients on the web.

We are a relationship management company that help build connections between professional music equipment manufacturers and high-volume professional music equipment users, i.e concert venue managers, equipment resellers, club owners, djs,etc.

We would like to see designs to incorporate the following:

- If possible a music theme tastefully designed into the company name/logo on the wordpress home page (not a dealbreaker without)

-We are choosing the Wordpress CMS because we're looking for the site to be more centered around our blog, which will be the main medium where we connect with clients and potential clients, where these previously strangers that we meet briefly on our travelings can get to know us better by coming to the site. The relationship, and the rapport that they feel towards my team and I, will be the key driver in determining whether they will want to do business through us or not. The products are secondary in importance. It is after the visitor feel comfortable doing business through us that they will venture to check out the products that we offer. Finally, the website is not a sales point, there will not be a feature for someone to buy something from the site.

Long story short, this website is meant to be a communications channel and not a sales channel.

-Need a contacts form application built-in to capture interested client information to facilitate the off-site sales process.

- Would prefer the theme to give a minimalist and conservative feel, and ideally capture the concept of our globalized world and the synergizing role that music plays in bringing people together.

-Ideally the design should incorporate subtle references to the Generation Y values that inspired our company name and mission:

-Emphasis on partnership and teamwork
-Belief and aspiration for win/win trade relations
-Fast, honest, and transparent service
-Make the world a better place via trade

Theme example (function-wise): http://demo2.larkpanes.com/?name=smpl

Product Type examplex: http://www.qolv.com.cn/en/product.asp

(Willing to pay extra if the winning design can be coded to full functionality)
Updates

To all those designers who've accepted the contest invitation, can you please send me a quick message to confirm if you are still planning on submitting by the end of the day tomorrow, 8/9. Otherwise we will make a selection ahead of the deadline so we can speed up our website live date. Thanks!

Target Market(s)

High volume/frequency professional music equipment users/resellers. Concert venues, DJs, Dance Clubs, etc

Industry/Entity Type

Communications

Requirements
Must have
• Blog
Product Showcase Page that is easy to update and expand.
About Page
Contact Forms Application built-in
Nice to have
• Music theme designed into company name/logo

```html
<!DOCTYPE html>
<html lang="en">
<head>
<meta charset="utf-8">
<title>Pellwick Trading Co — Connecting Musicians and Manufacturers</title>
<link rel="stylesheet" href="https://fonts.googleapis.com/css2?family=Open+Sans:wght@400;600;700&family=PT+Sans+Narrow:wght@400;700&display=swap">
<style>
  :root {
    --teal: #1bb5cc;
    --teal-text: #22b2c6;
    --header-bg: #13070f;
    --page-bg: #e9e9e7;
    --panel-bg: #f7f7f7;
    --card-bg: #ececec;
    --ink: #555555;
    --muted: #7a7a7a;
    --heading-grey: #9a9a9a;
    --dark-bar: #2b2b2b;
    --footer-bg: #262626;
    --footer-outer: #303030;
    --ribbon: #c42a2a;
    --white: #ffffff;
    --field-border: #c9c9c9;
  }
  * { box-sizing: border-box; margin: 0; padding: 0; }
  html, body { width: 1200px; height: 1169px; overflow: hidden; }
  body {
    position: relative;
    background: var(--page-bg);
    font-family: "Open Sans", Arial, sans-serif;
    color: var(--ink);
  }
  .abs { position: absolute; }

  /* Header */
  .site-header { left: 0; top: 0; width: 1200px; height: 65px; background: var(--header-bg); }
  .brand { left: 138px; top: 9px; display: flex; align-items: center; gap: 8px; }
  .brand-mark { width: 14px; height: 14px; border-radius: 50%; background: var(--teal); }
  .brand-name {
    font-family: "PT Sans Narrow", Arial, sans-serif; font-weight: 700;
    font-size: 22px; line-height: 24px; color: var(--teal); letter-spacing: 1px;
    width: 120px;
  }
  .main-nav { top: 24px; left: 0; width: 1200px; height: 18px; }
  .main-nav a {
    position: absolute; font-family: "PT Sans Narrow", Arial, sans-serif;
    font-size: 14px; color: var(--teal-text); text-decoration: none; letter-spacing: .2px;
  }
  .main-nav a.is-current { color: var(--white); }

  /* Hero */
  .hero { left: 0; top: 65px; width: 1200px; height: 438px;
    background:
      radial-gradient(ellipse at 70% 30%, rgba(210,180,140,.55), transparent 55%),
      radial-gradient(ellipse at 20% 85%, rgba(60,140,190,.55), transparent 50%),
      radial-gradient(ellipse at 85% 85%, rgba(70,150,200,.5), transparent 50%),
      linear-gradient(180deg, #5d5650 0%, #3c3c40 45%, #28323c 100%);
  }
  .hero-box { left: 138px; top: 143px; width: 457px; height: 200px; background: rgba(15,15,15,.62); }
  .hero-title {
    left: 156px; top: 158px; font-family: "PT Sans Narrow", Arial, sans-serif; font-weight: 700;
    font-size: 45px; line-height: 54px; color: var(--white); letter-spacing: .5px;
  }
  .hero-rule { left: 155px; top: 271px; width: 438px; border-top: 2px dotted rgba(255,255,255,.5); }
  .hero-text { left: 157px; top: 285px; width: 440px; font-size: 11px; line-height: 15.5px; color: var(--white); }
  .hero-text a { color: var(--teal-text); text-decoration: none; }

  /* Intro bar */
  .intro-bar { left: 105px; top: 440px; width: 990px; height: 63px; background: var(--teal); }
  .intro-text {
    left: 140px; top: 456px; font-size: 22.5px; letter-spacing: 2.2px; color: var(--white); line-height: 30px;
  }
  .intro-divider { left: 804px; top: 449px; height: 46px; border-left: 1px dotted rgba(255,255,255,.7); }
  .signup-field { left: 835px; top: 456px; width: 197px; height: 31px; background: var(--white);
    border: 1px solid #9fdbe4; font-size: 11px; font-style: italic; color: #8a8a8a; padding: 8px 12px; letter-spacing: .8px; }
  .signup-btn { left: 1031px; top: 456px; width: 30px; height: 31px; background: #1b1b1b;
    display: flex; align-items: center; justify-content: center; }

  /* Content panel */
  .content-panel { left: 105px; top: 503px; width: 990px; height: 600px; background: var(--panel-bg); }

  .carousel-arrow { width: 54px; height: 58px; border-radius: 50%; background: #333; top: 625px; }
  .carousel-arrow svg { position: absolute; top: 21px; }

  .product-card { top: 530px; width: 211px; height: 237px; background: var(--card-bg); }
  .product-title {
    position: absolute; left: 0; top: 5px; width: 100%; text-align: center;
    font-size: 12.5px; letter-spacing: 1.2px; color: #444;
  }
  .product-title-rule { position: absolute; left: 8px; right: 8px; top: 24px; border-top: 2px solid #dcdcdc; }
  .product-photo { position: absolute; left: 8px; top: 29px; width: 196px; height: 139px; background: var(--white); }
  .product-photo span { position: absolute; inset: 10px 14px; display: block; border-radius: 3px; }
  .product-caption { position: absolute; left: 0; top: 176px; width: 100%; text-align: center;
    font-size: 11px; letter-spacing: .8px; color: #555; }
  .btn-more { position: absolute; top: 202px; left: 72px; width: 67px; height: 23px; background: var(--teal);
    color: var(--white); font-size: 11px; font-weight: 700; letter-spacing: .8px; text-align: center; line-height: 23px; }
  .ribbon { left: 983px; top: 527px; }

  /* Blog */
  .blog { left: 139px; top: 793px; width: 596px; height: 271px; background: #efefef; border-left: 5px solid var(--teal); }
  .blog-heading { left: 160px; top: 806px; font-family: "PT Sans Narrow", Arial, sans-serif; font-weight: 700;
    font-size: 26px; letter-spacing: 2.4px; color: var(--heading-grey); }
  .post-thumb { width: 89px; height: 89px; background: var(--white); box-shadow: 0 0 2px rgba(0,0,0,.2); padding: 6px; }
  .post-thumb span { display: block; width: 100%; height: 100%;
    background: linear-gradient(180deg, #b9b9b9 0%, #8d8d8d 55%, #5e5e5e 100%); }
  .post-meta { font-size: 11px; letter-spacing: 1px; color: var(--teal-text); }
  .post-body { width: 450px; font-size: 11px; line-height: 19.3px; color: var(--muted); letter-spacing: .6px; }
  .post-body a { color: var(--teal-text); text-decoration: none; }

  /* Contact */
  .contact-head { left: 760px; top: 794px; width: 300px; height: 23px; background: var(--dark-bar);
    color: var(--white); font-size: 12.5px; letter-spacing: 1.2px; padding-left: 15px; line-height: 23px; }
  .contact-panel { left: 760px; top: 825px; width: 300px; height: 239px; background: #efefef; }
  .contact-intro { left: 776px; top: 836px; font-size: 11px; letter-spacing: .8px; color: #666; }
  .field-label { width: 60px; text-align: right; font-size: 11px; letter-spacing: 1px; color: #555; line-height: 14px; }
  .field { background: var(--white); border: 1px solid var(--field-border); }
  .btn-send { left: 977px; top: 1022px; width: 68px; height: 26px; background: var(--teal); color: var(--white);
    font-size: 11.5px; font-weight: 700; letter-spacing: 1px; text-align: center; line-height: 26px; }

  /* Footer */
  .footer-outer { left: 0; top: 1108px; width: 1200px; height: 61px; background: var(--footer-outer); }
  .site-footer { left: 105px; top: 1103px; width: 990px; height: 66px; background: var(--footer-bg); }
  .footer-nav a { position: absolute; top: 1128px; font-family: "PT Sans Narrow", Arial, sans-serif;
    font-size: 11px; color: #aaa; text-decoration: none; }
  .footer-nav a.is-current { color: var(--teal-text); }
  .copyright { right: 139px; top: 1128px; font-family: "PT Sans Narrow", Arial, sans-serif; font-size: 11px; color: #ccc; }
  .copyright span { color: var(--teal-text); }
</style>
</head>
<body>

<header class="site-header abs">
  <div class="brand abs">
    <span class="brand-mark"></span>
    <span class="brand-name">PELLWICK TRADING</span>
  </div>
  <nav class="main-nav abs">
    <a class="is-current" style="left:655px">HOME</a>
    <a style="left:710px">ABOUT</a>
    <a style="left:766px">BLOG</a>
    <a style="left:815px">PRODUCTS</a>
    <a style="left:891px">TESTIMONIALS</a>
    <a style="left:984px">SERVICES</a>
    <a style="left:1054px">CONTACT</a>
  </nav>
</header>

<section class="hero abs" role="img" aria-label="Close-up of the knobs on a mixing console"></section>
<div class="hero-box abs"></div>
<h1 class="hero-title abs">CONNECTING MUSICIANS<br>AND MANUFACTURERS</h1>
<div class="hero-rule abs"></div>
<p class="hero-text abs">Lorem ipsum dolor sit amet, consectetur adipiscing elit. Curabitur tellus nisi, lobortis eget tincidunt sit amet Et omnis postulant cum <a>about us ▸</a></p>

<div class="intro-bar abs"></div>
<p class="intro-text abs">INTRODUCTION MESSAGE TEXT WILL GO HERE</p>
<div class="intro-divider abs"></div>
<div class="signup-field abs">add your email for updates</div>
<div class="signup-btn abs"><svg width="9" height="10" viewBox="0 0 9 10"><path d="M0 0 L9 5 L0 10 Z" fill="#1bb5cc"/></svg></div>

<main class="content-panel abs"></main>

<div class="carousel-arrow abs" style="left:112px"><svg style="left:10px" width="13" height="16" viewBox="0 0 13 16"><path d="M13 0 L0 8 L13 16 Z" fill="#1bb5cc"/></svg></div>
<div class="carousel-arrow abs" style="left:1036px"><svg style="left:31px" width="13" height="16" viewBox="0 0 13 16"><path d="M0 0 L13 8 L0 16 Z" fill="#1bb5cc"/></svg></div>

<article class="product-card abs" style="left:138px">
  <h3 class="product-title">PRODUCT NAME - 3653GA</h3><div class="product-title-rule"></div>
  <div class="product-photo" role="img" aria-label="Wireless microphone set with receiver"><span style="background:linear-gradient(180deg,#fff 0%,#e6e6e6 40%,#4dc5b2 75%,#2a8f80 100%)"></span></div>
  <p class="product-caption">Eget tincidunt sit amet</p>
  <div class="btn-more">more ▸</div>
</article>
<article class="product-card abs" style="left:378px">
  <h3 class="product-title">PRODUCT NAME - 3653GA</h3><div class="product-title-rule"></div>
  <div class="product-photo" role="img" aria-label="Stack of three rack-mount amplifiers"><span style="background:linear-gradient(180deg,#d8d8d8,#f2f2f2 30%,#cfcfcf 50%,#f2f2f2 70%,#cfcfcf)"></span></div>
  <p class="product-caption">Eget tincidunt sit amet</p>
  <div class="btn-more">more ▸</div>
</article>
<article class="product-card abs" style="left:617px">
  <h3 class="product-title">PRODUCT NAME - 3653GA</h3><div class="product-title-rule"></div>
  <div class="product-photo" role="img" aria-label="Studio mixing desk"><span style="background:linear-gradient(180deg,#2e3440,#4a5a78 45%,#8a9098 75%,#2c2c30)"></span></div>
  <p class="product-caption">Eget tincidunt sit amet</p>
  <div class="btn-more">more ▸</div>
</article>
<article class="product-card abs" style="left:853px">
  <h3 class="product-title" style="text-align:left;padding-left:14px;overflow:hidden;white-space:nowrap">PRODUCT NAME - 3653GA</h3><div class="product-title-rule"></div>
  <div class="product-photo" role="img" aria-label="Powered mixer in a black case"><span style="background:radial-gradient(ellipse at 50% 45%,#555 0%,#2e2e2e 60%,#1a1a1a 100%)"></span></div>
  <p class="product-caption">Eget tincidunt sit amet</p>
  <div class="btn-more">more ▸</div>
</article>
<svg class="ribbon abs" width="78" height="78" viewBox="0 0 78 78" aria-hidden="true">
  <path d="M0 0 H27 L77 50 V77 Z" fill="#c42a2a"/>
  <text x="42" y="33" transform="rotate(45 42 33)" text-anchor="middle" font-family="PT Sans Narrow, Arial, sans-serif" font-weight="700" font-size="15" fill="#fff" letter-spacing="1">NEW</text>
</svg>

<section class="blog abs"></section>
<h2 class="blog-heading abs">RECENT BLOG ENTRIES</h2>

<div class="post-thumb abs" style="left:157px;top:856px"><span role="img" aria-label="Guitarist in a white shirt and hat"></span></div>
<p class="post-meta abs" style="left:266px;top:861px">8th August 2012</p>
<p class="post-meta abs" style="left:638px;top:861px">6 comments</p>
<p class="post-body abs" style="left:266px;top:883px">Phasellus sit amet ullamcorper risus. Aliquam et libero viverra tortor mollis varius. Etiam gravida elit in ipsum ultricies ac posuere nisi luctus diculus mus. Aliquam justo lectus, dig. &nbsp;<a>read more ▸</a></p>

<div class="post-thumb abs" style="left:157px;top:960px"><span role="img" aria-label="Guitarist in a white shirt and hat"></span></div>
<p class="post-meta abs" style="left:266px;top:965px">8th August 2012</p>
<p class="post-meta abs" style="left:638px;top:965px">6 comments</p>
<p class="post-body abs" style="left:266px;top:987px">Phasellus sit amet ullamcorper risus. Aliquam et libero viverra tortor mollis varius. Etiam gravida elit in ipsum ultricies ac posuere nisi luctus diculus mus. Aliquam justo lectus, dig. &nbsp;<a>read more ▸</a></p>

<h2 class="contact-head abs">GET IN TOUCH FOR MORE INFO</h2>
<div class="contact-panel abs"></div>
<p class="contact-intro abs">Lorem ipsum dolor sit amet, consectetur</p>
<label class="field-label abs" style="left:753px;top:870px">Name</label>
<div class="field abs" style="left:822px;top:865px;width:225px;height:28px"></div>
<label class="field-label abs" style="left:753px;top:909px">Email</label>
<div class="field abs" style="left:822px;top:902px;width:225px;height:28px"></div>
<label class="field-label abs" style="left:749px;top:946px">Text</label>
<div class="field abs" style="left:822px;top:939px;width:225px;height:72px"></div>
<label class="field-label abs" style="left:753px;top:1020px">Referral Code</label>
<div class="field abs" style="left:822px;top:1022px;width:145px;height:27px"></div>
<div class="btn-send abs">send ▸</div>

<div class="footer-outer abs"></div>
<footer class="site-footer abs"></footer>
<nav class="footer-nav">
  <a class="is-current" style="left:138px">Home</a>
  <a style="left:183px">About</a>
  <a style="left:234px">News</a>
  <a style="left:279px">Products</a>
  <a style="left:341px">Testimonials</a>
  <a style="left:419px">Sale</a>
  <a style="left:460px">Contact</a>
</nav>
<p class="copyright abs"><span>Copyright 2012</span>&nbsp; All rights reserved</p>

</body>
</html>
```